Unique Elegant Stationary Set

Prepare a unique eye catching stationary set consisting of :
(1) Letterhead
(2) A3 Envelope
(3) Business Card
(4) Email Signature Banner

Package to be elegant, modern, and designers not only to think of design or colors but also materials could make a big difference, embossing, debossing, glossy, matt ....etc.

I attached both our new logos (Stacked or Linear) noting you may use any of them but you cant modify anything in the logos. Also attached our final draft portfolio to see what type of projects we work on and i also have here a glimboard page link showing the direction we want: https://www.glimboard.example/ravelkoton/business-card-design/

Target Market(s)

VVIP / Elite Developers

Industry/Entity Type

Architecture

Font styles to use
Sans Serif
Other font styles liked:
• unitext

Requirements
Should not have
• too many colors, or being busy in general. We want something pleasing to the eye

```html
<!DOCTYPE html>
<html lang="en">
<head>
<meta charset="utf-8">
<title>Varo Studio — Stationery</title>
<link rel="stylesheet" href="https://fonts.googleapis.com/css2?family=Lato:wght@400;700&display=swap">
<style>
  :root {
    --backdrop: #0e0e0e;
    --card-paper: #a4a4a4;
    --envelope-body: #9b9b9b;
    --envelope-pocket: #969696;
    --envelope-flap: #e4e4e4;
    --mark-tone: #878787;
    --mark-tone-large: #8c8c8c;
    --contact-ink: #f4f4f4;
  }
  html, body {
    margin: 0;
    padding: 0;
    width: 1200px;
    height: 806px;
    overflow: hidden;
    background: var(--backdrop);
    font-family: "Lato", Arial, sans-serif;
  }
  .stage {
    position: relative;
    width: 1200px;
    height: 806px;
  }
  .envelope {
    position: absolute;
    left: 507px;
    top: 148px;
    width: 558px;
    height: 452px;
  }
  .envelope-wordmark {
    position: absolute;
    left: 250px;
    top: 350px;
    width: 305px;
    height: 102px;
    overflow: hidden;
  }
  .envelope-wordmark span {
    display: block;
    font-weight: 700;
    font-size: 128px;
    line-height: 1;
    letter-spacing: 4px;
    color: var(--mark-tone-large);
    margin-top: -4px;
  }
  .letter-card {
    position: absolute;
    left: 172px;
    top: 322px;
    width: 558px;
    height: 371px;
    background: var(--card-paper);
    border-radius: 5px;
  }
  .card-wordmark {
    position: absolute;
    left: 22px;
    top: 298px;
    width: 124px;
    color: var(--mark-tone);
    font-weight: 700;
  }
  .card-wordmark .name-main {
    display: block;
    font-size: 40px;
    line-height: 38px;
    letter-spacing: 1px;
  }
  .card-wordmark .name-sub {
    display: block;
    font-size: 9px;
    letter-spacing: 11.5px;
    margin-top: 3px;
  }
  .contact-line {
    position: absolute;
    left: 158px;
    top: 345px;
    margin: 0;
    display: flex;
    align-items: center;
    gap: 6px;
    font-size: 6.2px;
    color: var(--contact-ink);
    white-space: nowrap;
    letter-spacing: 0.1px;
  }
  .contact-line .studio-name,
  .contact-line .building { font-weight: 700; font-size: 6.6px; }
  .contact-line .divider {
    display: inline-block;
    width: 0.6px;
    height: 8px;
    background: var(--contact-ink);
  }
  .contact-line .item {
    display: inline-flex;
    align-items: center;
    gap: 2px;
  }
  .contact-line svg { width: 7px; height: 7px; }
</style>
</head>
<body>
<main class="stage">

  <section class="envelope" aria-label="Envelope, back with open flap">
    <svg width="558" height="452" viewBox="0 0 558 452" xmlns="http://www.w3.org/2000/svg">
      <path class="flap" d="M0 83 L0 58 Q10 0 60 0 L498 0 Q548 0 558 58 L558 83 Z" fill="var(--envelope-flap)"/>
      <rect class="body" x="0" y="83" width="558" height="369" rx="4" fill="var(--envelope-body)"/>
      <path class="side-fold" d="M0 83 Q0 78 22 78 Q44 78 51 104 L558 104 L558 83 Q558 78 536 78 Q514 78 507 104 Z" fill="var(--envelope-body)"/>
      <path class="pocket" d="M19 130 Q19 104 45 104 L510 104 Q536 104 536 130 L543 452 L19 452 Z" fill="var(--envelope-pocket)"/>
    </svg>
    <div class="envelope-wordmark"><span>VARO</span></div>
  </section>

  <section class="letter-card" aria-label="Letterhead card">
    <div class="card-wordmark">
      <span class="name-main">VARO</span>
      <span class="name-sub">STUDIO</span>
    </div>
    <p class="contact-line">
      <span class="studio-name">VARO STUDIO</span>
      <span class="divider"></span>
      <span><span class="building">HALDEN TOWER,</span> 14th FLOOR, 1402, P.O. BOX: 20519</span>
      <span class="divider"></span>
      <span class="item">
        <svg viewBox="0 0 10 10" aria-hidden="true"><circle cx="5" cy="5" r="4.4" fill="none" stroke="currentColor" stroke-width="0.7"/><path d="M3.4 2.8 L4.2 2.6 L4.7 3.9 L4.2 4.3 Q4.7 5.4 5.7 5.9 L6.1 5.4 L7.3 5.9 L7.1 6.7 Q5.6 7.3 4.2 5.8 Q3 4.4 3.4 2.8 Z" fill="currentColor"/></svg>
        +000 2 555 0142
      </span>
      <span class="item">
        <svg viewBox="0 0 10 10" aria-hidden="true"><circle cx="5" cy="5" r="4.4" fill="none" stroke="currentColor" stroke-width="0.7"/><rect x="2.7" y="3.3" width="4.6" height="3.4" fill="none" stroke="currentColor" stroke-width="0.6"/><path d="M2.7 3.3 L5 5.2 L7.3 3.3" fill="none" stroke="currentColor" stroke-width="0.6"/></svg>
        INFO@VAROSTUDIO.EXAMPLE
      </span>
    </p>
  </section>

</main>
</body>
</html>
```